User Frontend Design for Support Logging System

I have a PHP web application to manage IT support calls and require a front-end design and user logon screen.

I have attached the current design which needs improving.

I have 2 current designs. The 2nd design is one I have been working on but requires a "professional touch". I also require the tables designed with dummy data from the 1st design.

I have attached my company logo in AI format which I would like incorporated into the design. There should also be a placeholder to supply the users company name upon login.

The screenshots I have attached should explain what I am looking for.

The Home Page should include charts which show statistical information such as:
Number of support tickets logged per month. Bar Chart etc.
Number of currently open support tickets.
Number of Quote Requests awaiting a response.
Number of Files and file repository.
Number of Reports.
Number of Customers.

For the Jobs and Customers pages the table fields should be designed as per the attached screenshots but a better looking tables. The table options such as uploading a file and adding a customer - these options can be changed and displayed differently.

Quotes page should display quotes returned and a "request a quote form".

Files page should have a good structure for browsing through an archive of files.

Profile page should have the option to include a profile picture.

An additional side page should be created for a web based calendar (these calendar entries will be updated by code).

The navbar should also include an alerts section.
The current attached design I have is based on bootstraps navbar.

Inspiration: http://pelvoriad.com/freebie/free-admin-templates-for-backend-panels/

Hopefully this above link will show you some navigation style designs that I am looking for.

Please note, I will be doing the PHP coding myself and it is just the page designs I require in either HTML and or PHP format. I also require the CSS files for this project.
I need the code in a format where I can add and remove items in the menu from the code and not PSD/image based format.

If you think this project requires a higher budget let me know what you would expect and I will increase it!

Any questions, please let me know.
Dummy data can be shown for design purposes.

I have provided you a dummy login to our current system to show you the system:
https://ridge.brivelnetworks.co.uk/
username: dan.prewett@brivelnetworks.co.uk
password:P@55w0rd

```html
<!DOCTYPE html>
<html lang="en">
<head>
<meta charset="utf-8">
<title>Reports Table – Brivel Networks</title>
<link href="https://fonts.googleapis.com/css2?family=Arimo:wght@400;700&family=Raleway:wght@300;400&display=swap" rel="stylesheet">
<style>
:root{
  --page:#ffffff;
  --sidebar:#f5f5f5;
  --line:#dddddd;
  --line-soft:#e6e6e6;
  --text:#333333;
  --muted:#777777;
  --link:#428bca;
  --brand:#1b3f8b;
  --active:#0a8cf5;
  --icon:#3d8ee0;
  --badge:#1c7cf0;
  --chip:#dfe1e3;
  --check:#d7dadd;
  --warn:#f0ad4e;
  --ok:#5cb85c;
  --bad:#d9534f;
  --flag:#444444;
  --panel-head:#f3f3f5;
}
*{box-sizing:border-box;margin:0;padding:0}
html,body{width:1200px;height:755px;overflow:hidden}
body{position:relative;background:var(--page);font-family:"Arimo",Arial,sans-serif;color:var(--text);font-size:12px}

/* top bar */
.topbar{position:absolute;left:0;top:0;width:1200px;height:42px;border-bottom:1px solid var(--line);background:var(--page)}
.brand{position:absolute;left:22px;top:7px;display:flex;align-items:center;gap:6px}
.brand-dot{width:28px;height:28px;border-radius:50%;border:2px solid var(--brand)}
.brand-name{font-weight:700;font-size:15px;color:var(--brand)}
.alert{position:absolute;top:8px;width:26px;height:26px}
.alert svg{position:absolute;left:6px;top:8px}
.badge{position:absolute;left:-4px;top:0;min-width:17px;height:13px;padding:0 4px;border-radius:7px;background:var(--badge);color:#fff;font-size:9px;line-height:13px;text-align:center}
.user{position:absolute;left:1027px;top:8px;display:flex;align-items:center;gap:5px}
.avatar{width:26px;height:26px;border-radius:50%;background:radial-gradient(circle at 50% 40%,#b89a86,#5a4a42)}
.user-name{font-size:14.5px;color:#555}

/* sidebar */
.sidebar{position:absolute;left:0;top:42px;width:201px;height:676px;background:var(--sidebar);border-right:1px solid var(--line)}
.collapse{position:absolute;left:156px;top:10px;width:26px;height:26px;background:var(--chip);display:flex;align-items:center;justify-content:center;gap:5px;color:#aaa;font-size:11px}
.nav{position:absolute;left:0;top:45px;width:200px;list-style:none}
.nav li{position:relative;height:36.5px;border-bottom:1px solid var(--line);display:flex;align-items:center;padding-left:13px;gap:8px;font-size:13px;color:#444}
.nav li svg{width:15px;height:15px;fill:none;stroke:var(--icon);stroke-width:1.4}
.nav li.is-active{background:var(--active);color:#fff;border-bottom-color:var(--active)}
.nav li.is-active svg{stroke:#fff}
.nav li.is-active::after{content:"";position:absolute;right:-9px;top:0;border-left:9px solid var(--active);border-top:18px solid transparent;border-bottom:18.5px solid transparent}

/* content */
.crumbs{position:absolute;left:201px;top:42px;width:999px;height:45px;border-bottom:1px solid var(--line);background:#f7f7f7}
.crumb-trail{position:absolute;left:13px;top:15px;display:flex;align-items:center;gap:7px;font-size:12px;color:#777}
.crumb-trail a{color:var(--link);text-decoration:none}
.search{position:absolute;left:843px;top:12px;width:147px;height:23px;background:var(--chip);border-radius:4px;padding-left:8px;font-size:12.5px;line-height:23px;color:#a5a5a5}
.search svg{position:absolute;right:8px;top:4px}
.page-title{position:absolute;left:215px;top:102px;font-family:"Raleway",sans-serif;font-weight:300;font-size:34px;color:#555;white-space:nowrap}
.page-title small{font-size:13px;color:#888;font-weight:400;margin-left:4px}
.rule{position:absolute;left:214px;top:162px;width:973px;border-top:1px solid var(--line-soft)}

.panel{position:absolute;left:214px;top:181px;width:973px;height:500px;border:1px solid var(--line);border-radius:3px}
.panel-head{height:33px;background:var(--panel-head);border-bottom:1px solid var(--line);position:relative}
.panel-icon{position:absolute;left:0;top:0;width:29px;height:32px;border-right:1px solid var(--line);display:flex;align-items:center;justify-content:center}
.panel-title{position:absolute;left:37px;top:10px;font-size:12.5px}
.panel-tools{position:absolute;right:7px;top:10px;display:flex;gap:9px;font-size:11px;color:#555}

.report{position:absolute;left:15px;top:45px;width:943px;border-collapse:collapse;font-size:12px}
.report th,.report td{border-bottom:1px solid var(--line);text-align:left;padding-left:8px;height:38.2px}
.report th{height:39px;font-weight:700;color:#555;border-bottom:2px solid var(--line);border-left:1px solid var(--line)}
.report td{border-left:1px solid var(--line)}
.report tr th:first-child,.report tr td:first-child{border-left:0;padding-left:0;text-align:center}
.report{border:1px solid var(--line)}
.check{display:inline-block;width:18px;height:18px;border-radius:3px;background:var(--check);vertical-align:middle}
.report a{color:var(--link);text-decoration:none}
.status{display:inline-block;padding:0 5px;height:20px;line-height:20px;border-radius:2px;color:#fff;font-weight:700;font-size:10px}
.status--expiring{background:var(--warn)}
.status--registered{background:var(--ok)}
.status--expired{background:var(--bad)}
.status--flagged{background:var(--flag)}

.footer{position:absolute;left:0;top:718px;width:1200px;height:37px;background:var(--sidebar);border-top:1px solid var(--line)}
.footer p{position:absolute;left:18px;top:11px;font-size:11px;color:#555}
.to-top{position:absolute;left:1156px;top:6px;width:27px;height:27px;background:#e9e9e9;display:flex;align-items:center;justify-content:center}
</style>
</head>
<body>
<header class="topbar">
  <div class="brand"><span class="brand-dot"></span><span class="brand-name">Brivel Networks</span></div>
  <div class="alert" style="left:895px"><svg width="14" height="12" viewBox="0 0 14 12" fill="#999"><rect x="0" y="0" width="3" height="2.5"/><rect x="4" y="0" width="10" height="2.5"/><rect x="0" y="4.5" width="3" height="2.5"/><rect x="4" y="4.5" width="10" height="2.5"/><rect x="0" y="9" width="3" height="2.5"/><rect x="4" y="9" width="10" height="2.5"/></svg><span class="badge">12</span></div>
  <div class="alert" style="left:938px"><svg width="14" height="14" viewBox="0 0 14 14"><circle cx="7" cy="7" r="7" fill="#999"/><rect x="6" y="3" width="2" height="5.5" fill="#fff"/><rect x="6" y="9.5" width="2" height="2" fill="#fff"/></svg><span class="badge">11</span></div>
  <div class="alert" style="left:986px"><svg width="15" height="13" viewBox="0 0 15 13" fill="#999"><path d="M0 0h11v8H4l-3 3V8H0z"/><path d="M12 3h3v7h-1v3l-3-3H6v-1h6z"/></svg><span class="badge">9</span></div>
  <div class="user"><span class="avatar" role="img" aria-label="User profile photo"></span><span class="user-name">Owen Halbrook</span><svg width="9" height="6" viewBox="0 0 9 6"><path d="M1 1l3.5 3.5L8 1" fill="none" stroke="#aaa" stroke-width="1.2"/></svg></div>
</header>

<aside class="sidebar">
  <div class="collapse"><span>‹</span><span>›</span></div>
  <ul class="nav">
    <li class="is-active"><svg viewBox="0 0 16 16"><path d="M2 8l6-6 6 6M4 6.5V14h3v-4h2v4h3V6.5"/></svg>Dashboard</li>
    <li><svg viewBox="0 0 16 16"><rect x="1" y="2" width="14" height="9"/><path d="M5 14h6M8 11v3"/></svg>Jobs</li>
    <li><svg viewBox="0 0 16 16"><path d="M3 1l10 7-4.5 1 2.5 5-2 1-2.5-5L3 13z"/></svg>Customers</li>
    <li><svg viewBox="0 0 16 16"><circle cx="8" cy="8" r="2.5"/><circle cx="8" cy="8" r="6" stroke-dasharray="3 1.6"/></svg>Inventory</li>
    <li><svg viewBox="0 0 16 16"><rect x="1" y="2" width="14" height="12"/><path d="M1 6h14M1 10h14M6 2v12M10.5 2v12"/></svg>Reports</li>
    <li><svg viewBox="0 0 16 16"><path d="M9 2H1v13h13V7"/><path d="M6 10l1-3 7-6 2 2-7 6z"/></svg>Files</li>
    <li><svg viewBox="0 0 16 16"><circle cx="8" cy="5" r="3.5"/><path d="M1 15c0-4 3-6 7-6s7 2 7 6z"/></svg>Quotes</li>
  </ul>
</aside>

<nav class="crumbs">
  <div class="crumb-trail">
    <svg width="16" height="13" viewBox="0 0 16 13" fill="none" stroke="#aaa"><rect x=".5" y=".5" width="15" height="12"/><path d="M.5 4.5h15M.5 8.5h15M5.5.5v12M10.5.5v12"/></svg>
    <a href="#">Home</a><span style="color:#ccc">/</span><span>&nbsp;Reports Tables</span>
  </div>
  <div class="search">Start Searching...<svg width="15" height="15" viewBox="0 0 15 15" fill="none" stroke="#999" stroke-width="1.6"><circle cx="6" cy="6" r="5"/><path d="M10 10l4 4"/></svg></div>
</nav>

<h1 class="page-title">Reports Table<small>report tables samples</small></h1>
<div class="rule"></div>

<section class="panel">
  <div class="panel-head">
    <div class="panel-icon"><svg width="11" height="11" viewBox="0 0 11 11"><rect width="11" height="11" rx="2" fill="#444"/><path d="M3 8l5-5M5 3h3v3" stroke="#fff" stroke-width="1.3" fill="none"/></svg></div>
    <span class="panel-title">Table xyz</span>
    <div class="panel-tools">
      <svg width="11" height="11" viewBox="0 0 11 11"><path d="M1 3l4.5 4.5L10 3" fill="none" stroke="#444" stroke-width="2"/></svg>
      <svg width="11" height="11" viewBox="0 0 11 11"><path d="M1 10l5-5M6 5a3 3 0 1 0 0-.1" fill="none" stroke="#555" stroke-width="1.8"/></svg>
      <svg width="11" height="11" viewBox="0 0 11 11"><path d="M9 4a4 4 0 1 0 0 3M9 1v3H6" fill="none" stroke="#555" stroke-width="1.6"/></svg>
      <span style="width:14px"></span>
      <svg width="10" height="10" viewBox="0 0 10 10"><path d="M2 2l6 6M8 2l-6 6" stroke="#444" stroke-width="2"/></svg>
    </div>
  </div>
  <table class="report">
    <colgroup><col style="width:100px"><col style="width:214px"><col style="width:119px"><col style="width:129px"><col style="width:158px"><col></colgroup>
    <thead><tr><th><span class="check"></span></th><th>Domain</th><th>Price</th><th>Clicks</th><th>Update</th><th>Status</th></tr></thead>
    <tbody>
      <tr><td><span class="check"></span></td><td><a href="#">alpha.com</a></td><td>$45</td><td>3,330</td><td>Feb 13</td><td><span class="status status--expiring">Expiring</span></td></tr>
      <tr><td><span class="check"></span></td><td><a href="#">beta.com</a></td><td>$70</td><td>3,330</td><td>Jen 15</td><td><span class="status status--registered">Registered</span></td></tr>
      <tr><td><span class="check"></span></td><td><a href="#">gamma.com</a></td><td>$25</td><td>3,330</td><td>Mar 09</td><td><span class="status status--expired">Expired</span></td></tr>
      <tr><td><span class="check"></span></td><td><a href="#">delta.com</a></td><td>$50</td><td>3,330</td><td>Feb 10</td><td><span class="status status--flagged">Flagged</span></td></tr>
      <tr><td><span class="check"></span></td><td><a href="#">epsilon.com</a></td><td>$35</td><td>3,330</td><td>Feb 18</td><td><span class="status status--registered">Registered</span></td></tr>
      <tr><td><span class="check"></span></td><td><a href="#">zeta.com</a></td><td>$45</td><td>3,330</td><td>Feb 13</td><td><span class="status status--expiring">Expiring</span></td></tr>
      <tr><td><span class="check"></span></td><td><a href="#">eta.com</a></td><td>$70</td><td>3,330</td><td>Jen 15</td><td><span class="status status--registered">Registered</span></td></tr>
      <tr><td><span class="check"></span></td><td><a href="#">theta.com</a></td><td>$25</td><td>3,330</td><td>Mar 09</td><td><span class="status status--expired">Expired</span></td></tr>
      <tr><td><span class="check"></span></td><td><a href="#">iota.com</a></td><td>$50</td><td>3,330</td><td>Feb 10</td><td><span class="status status--flagged">Flagged</span></td></tr>
      <tr><td><span class="check"></span></td><td><a href="#">kappa.com</a></td><td>$35</td><td>3,330</td><td>Feb 18</td><td><span class="status status--registered">Registered</span></td></tr>
    </tbody>
  </table>
</section>

<footer class="footer">
  <p>2014 © Brivel Networks ltd.</p>
  <div class="to-top"><svg width="10" height="6" viewBox="0 0 10 6"><path d="M1 5l4-4 4 4" fill="none" stroke="#bbb" stroke-width="1.2"/></svg></div>
</footer>
</body>
</html>
```